Dulwick Medical

Need smart and sleek business cards design for my medical distribution company. use logos attached.

add my details

Harriet Colbeck
Director/Sales Agent
harriet@dulwickmedical.com.au
0461 835 207

```html
<!DOCTYPE html>
<html lang="en">
<head>
<meta charset="UTF-8">
<title>Dulwick Medical – Business Cards</title>
<link href="https://fonts.googleapis.com/css2?family=Montserrat:wght@500;600;700;800&display=swap" rel="stylesheet">
<style>
  :root {
    --navy: #0d2466;
    --navy-deep: #0a1d55;
    --blue: #2a86bd;
    --blue-soft: #5aa7d6;
    --white: #ffffff;
    --card-white: #fbfbfc;
    --backdrop: #d9dbe0;
  }
  * { margin: 0; padding: 0; box-sizing: border-box; }
  html, body { width: 1200px; height: 900px; overflow: hidden; }
  body {
    background: var(--backdrop);
    font-family: "Montserrat", Arial, sans-serif;
  }
  .sheet {
    width: 1200px; height: 900px;
    display: flex; flex-direction: column;
    align-items: center; justify-content: center;
    gap: 44px;
  }
  .card {
    position: relative;
    width: 640px; height: 390px;
    border-radius: 24px;
    overflow: hidden;
    box-shadow: 0 8px 24px rgba(0,0,0,0.18);
  }
  /* Back of card */
  .card--back { background: var(--navy); }
  .card--back .feature-art {
    position: absolute; left: 0; top: 0;
    width: 640px; height: 390px;
  }
  .card--back .brand {
    position: absolute; right: 56px; top: 52px;
    text-align: right;
  }
  .brand-name {
    font-weight: 800;
    font-size: 30px;
    letter-spacing: 0.5px;
    text-transform: uppercase;
    line-height: 1;
  }
  .card--back .brand-name { color: var(--white); }
  .website {
    margin-top: 16px;
    font-weight: 500;
    font-size: 17px;
    color: var(--blue-soft);
  }
  /* Front of card */
  .card--front { background: var(--card-white); }
  .card--front .brand {
    position: absolute; right: 52px; top: 58px;
  }
  .card--front .brand-name { color: var(--navy); }
  .contact {
    position: absolute; left: 52px; bottom: 52px;
    color: var(--navy);
  }
  .contact-name {
    font-weight: 800; font-size: 24px; text-transform: uppercase;
    letter-spacing: 0.3px;
  }
  .contact-role {
    margin-top: 4px;
    font-weight: 500; font-size: 17px; text-transform: uppercase;
    color: var(--blue);
  }
  .divider {
    width: 52px; height: 2px; background: var(--blue);
    margin: 18px 0 14px;
  }
  .contact-line {
    font-weight: 600; font-size: 19px; line-height: 1.35;
  }
  .contact-line .label { color: var(--blue); margin-right: 6px; }
</style>
</head>
<body>
<main class="sheet">
  <section class="card card--back">
    <svg class="feature-art" viewBox="0 0 640 390" role="img" aria-label="Large abstract knee-joint artwork in white, navy and blue sweeping across the lower left">
      <defs>
        <linearGradient id="artTone" x1="0" y1="0" x2="1" y2="1">
          <stop offset="0" stop-color="#eef2f8"/>
          <stop offset="0.55" stop-color="#c9dbec"/>
          <stop offset="1" stop-color="#2a86bd"/>
        </linearGradient>
      </defs>
      <path d="M0 110 C140 95 300 90 350 120 L520 390 L0 390 Z" fill="url(#artTone)"/>
    </svg>
    <div class="brand">
      <div class="brand-name">Dulwick Medical</div>
      <div class="website">dulwickmedical.com.au</div>
    </div>
  </section>

  <section class="card card--front">
    <div class="brand">
      <div class="brand-name">Dulwick Medical</div>
    </div>
    <div class="contact">
      <div class="contact-name">Harriet Colbeck</div>
      <div class="contact-role">Director/Sales Agent</div>
      <div class="divider"></div>
      <div class="contact-line"><span class="label">P</span>0461 835 207</div>
      <div class="contact-line"><span class="label">E</span>harriet@dulwickmedical.com.au</div>
    </div>
  </section>
</main>
</body>
</html>
```